Corvenda

I need a professional web site that is directed at the energy industry, Oil, Gas, Mining
I need the website to have the usual pages
1. home page
2. news page.
3. contact us page
4. About us
and a CMS admin section to add further pages and content
Must be Google friendly with SEO facility

Target Market(s)

energy industry, Oil, Gas, Mining

Industry/Entity Type

Industry

Font styles to use
Sans Serif

Colors
faa54b
85cae6
cadf82

Requirements
Must have
• social media icons
site map

```html
<!DOCTYPE html>
<html lang="en">
<head>
<meta charset="utf-8">
<title>Corvenda – Energy Industry</title>
<link rel="stylesheet" href="https://fonts.googleapis.com/css2?family=Roboto:ital,wght@0,400;0,500;0,700;1,400&display=swap">
<style>
:root{
  --orange:#faa54b;
  --sky:#85cae6;
  --lime:#cadf82;
  --navy:#1e2b3a;
  --navy-deep:#15202b;
  --footer:#0d0e10;
  --white:#ffffff;
  --grey:#a9b0b8;
  --btn:#e9e9e9;
  --btn-text:#333a42;
  --header-bg:#eef3f8;
  --text-dark:#3b4048;
}
*{box-sizing:border-box;margin:0;padding:0}
html,body{width:1200px;height:2195px;overflow:hidden}
body{position:relative;font-family:"Roboto",Arial,sans-serif;color:var(--white);background:var(--navy)}
a{color:inherit;text-decoration:none}
.abs{position:absolute}

/* header */
.site-header{position:absolute;left:0;top:0;width:1200px;height:102px;background:linear-gradient(180deg,#f7f9fb,var(--header-bg));border-bottom:1px solid #c9d2db}
.brand{position:absolute;left:91px;top:32px;display:flex;align-items:center;gap:10px;font-weight:700;font-size:30px;letter-spacing:1px;color:#1b1d21}
.brand-mark{width:14px;height:14px;background:var(--orange)}
.main-nav{position:absolute;top:46px;font-size:14.5px;color:var(--text-dark)}
.main-nav a{position:absolute;white-space:nowrap}
.main-nav .active{color:var(--orange)}
.login-btn{position:absolute;left:1036px;top:38px;width:73px;height:32px;border:1.5px solid var(--orange);border-radius:2px;color:var(--orange);font-size:14px;text-align:center;line-height:29px}

/* hero */
.hero{position:absolute;left:0;top:102px;width:1200px;height:542px;background:linear-gradient(180deg,#8fb0cf 0%,#7c8a96 28%,#5b5f62 55%,#6d6860 100%)}
.hero-caption{position:absolute;left:91px;top:208px;width:707px;height:123px;background:rgba(20,22,25,.72)}
.hero-title{position:absolute;left:21px;top:22px;font-size:29px;font-weight:700}
.hero-sub{position:absolute;left:24px;top:65px;font-size:23px}
.slider-dots{position:absolute;left:539px;top:495px;display:flex;gap:9px}
.slider-dots span{width:17px;height:17px;border-radius:50%;background:var(--white)}
.slider-dots .current{background:var(--orange)}

/* sections */
.welcome{position:absolute;left:0;top:644px;width:1200px;height:234px;background:var(--navy);text-align:center}
.section-title{font-size:25px;font-weight:700;text-transform:uppercase}
.welcome .section-title{position:absolute;left:0;right:0;top:44px;color:var(--lime)}
.welcome-text{position:absolute;left:115px;right:115px;top:90px;font-size:14.5px;line-height:30px}
.btn{display:block;background:linear-gradient(180deg,#fafafa,var(--btn));color:var(--btn-text);font-size:13px;font-weight:500;text-align:center;border-radius:3px;box-shadow:0 2px 2px rgba(0,0,0,.4)}
.welcome .btn{position:absolute;left:528px;top:167px;width:122px;height:35px;line-height:35px}

.services{position:absolute;left:0;top:878px;width:1200px;height:615px;background:var(--navy-deep)}
.services .section-title{position:absolute;left:0;right:0;top:53px;text-align:center;color:var(--orange)}
.section-sub{position:absolute;left:0;right:0;text-align:center;font-size:17px}
.services .section-sub{top:101px}
.service{position:absolute;top:165px;width:313px}
.service-photo{width:313px;height:217px;border:4px solid var(--white)}
.service h3{margin-top:14px;font-size:25px;font-weight:700;color:var(--orange)}
.service p{margin-top:8px;font-size:15px;line-height:23.5px;text-align:justify}
.service .btn{margin-top:12px;width:123px;height:35px;line-height:35px}

.news{position:absolute;left:0;top:1493px;width:1200px;height:336px;background:var(--navy)}
.news .section-title{position:absolute;left:0;right:0;top:46px;text-align:center;color:var(--sky);font-weight:500}
.news .section-sub{top:88px}
.news-item{position:absolute;top:164px;width:310px}
.news-date{display:flex;align-items:center;gap:9px;font-size:17px;color:var(--lime)}
.news-item h4{margin-top:11px;font-size:17px;font-weight:400;color:var(--sky)}
.news-item p{margin-top:2px;font-size:11px;line-height:18px}
.news-item .more{color:var(--orange);margin-left:8px}

/* footer */
.site-footer{position:absolute;left:0;top:1829px;width:1200px;height:237px;background:var(--footer)}
.footer-col{position:absolute;top:47px}
.footer-col h5{font-size:17px;font-weight:400;color:var(--lime);margin-bottom:12px}
.footer-col li{list-style:none;font-size:14px;line-height:23.4px}
.testimonial{width:240px;font-size:12px;font-style:italic;line-height:18.6px;padding-left:10px}
.testimonial-author{font-size:11px;color:#2c3036;margin-top:6px;padding-left:10px}
.newsletter p{width:240px;font-size:13.5px;line-height:17px;color:var(--grey);margin-top:-4px}
.email-field{margin-top:10px;width:230px;height:32px;background:#ececec;border:1px solid #bbb;color:#777;font-size:13px;line-height:30px;padding-left:10px}
.subscribe-btn{margin-top:10px;width:91px;height:29px;background:var(--orange);border-radius:2px;font-size:12px;font-weight:500;text-align:center;line-height:29px}

.bottom-bar{position:absolute;left:0;top:2066px;width:1200px;height:129px;background:var(--navy)}
.legal-links{position:absolute;left:110px;top:44px;font-size:13px}
.legal-links span{margin:0 7px}
.copyright{position:absolute;left:110px;top:67px;font-size:13px}
.social{position:absolute;left:910px;top:53px;display:flex;gap:1.5px}
.social span{width:31px;height:31px}
</style>
</head>
<body>

<header class="site-header">
  <div class="brand"><span class="brand-mark"></span>Corvenda</div>
  <nav class="main-nav">
    <a class="active" style="left:580px">HOME</a>
    <a style="left:651px">ABOUT US</a>
    <a style="left:749px">INDUSTRIES</a>
    <a style="left:860px">NEWS</a>
    <a style="left:928px">CONTACT US</a>
  </nav>
  <a class="login-btn">LOGIN</a>
</header>

<section class="hero" role="img" aria-label="Photo of a large yellow excavator and orange mining dump truck in an open pit quarry under a blue sky">
  <div class="hero-caption">
    <div class="hero-title">ENERGY INDUSTRY</div>
    <div class="hero-sub">Lorem Ipsum has been the industry's standard dummy text</div>
  </div>
  <div class="slider-dots"><span class="current"></span><span></span><span></span><span></span><span></span></div>
</section>

<section class="welcome">
  <h2 class="section-title">Welcome to Corvenda</h2>
  <p class="welcome-text">Lorem Ipsum has been the industry's standard dummy text ever since the 1500s, when an unknown printer took a galley of type and scrambled it to make a type specimen book. It has survived not only five centuries, but also the leap into electronic typesetting, remaining essentially unchanged</p>
  <a class="btn">READ MORE</a>
</section>

<section class="services">
  <h2 class="section-title">We are competent in our service</h2>
  <p class="section-sub">Lorem Ipsum is simply dummy text of the printing and typesetting industry</p>

  <article class="service" style="left:88px">
    <div class="service-photo" role="img" aria-label="Oil pumpjacks silhouetted against a golden sunset" style="background:radial-gradient(circle at 45% 60%,#fff6c0 0%,#f5c642 30%,#c7801c 75%,#7a4a12 100%)"></div>
    <h3>OIL</h3>
    <p>Lorem Ipsum has been the industry's standard dummy text ever since the 1500s, when an unknown printer took a galley</p>
    <a class="btn">READ MORE</a>
  </article>

  <article class="service" style="left:445px">
    <div class="service-photo" role="img" aria-label="Row of white spherical gas storage tanks" style="background:linear-gradient(180deg,#b9c2c9 0%,#e6e9ec 45%,#c9cfd3 75%,#8f9a8d 100%)"></div>
    <h3>GAS</h3>
    <p>Lorem Ipsum has been the industry's standard dummy text ever since the 1500s, when an unknown printer took a galley</p>
    <a class="btn">READ MORE</a>
  </article>

  <article class="service" style="left:798px">
    <div class="service-photo" role="img" aria-label="Excavator loading a yellow dump truck at a mining site" style="background:linear-gradient(180deg,#8a8c8d 0%,#5f6061 45%,#4a4a48 70%,#2f2e2b 100%)"></div>
    <h3>MINING</h3>
    <p>Lorem Ipsum has been the industry's standard dummy text ever since the 1500s, when an unknown printer took a galley</p>
    <a class="btn">READ MORE</a>
  </article>
</section>

<section class="news">
  <h2 class="section-title">Latest News</h2>
  <p class="section-sub">Quisque porttitor sem liberoet auctor lorem fringilla sit amehasellus gravida nisi elitam</p>

  <article class="news-item" style="left:88px">
    <div class="news-date"><svg width="17" height="17" viewBox="0 0 17 17"><rect x="1" y="3" width="15" height="13" fill="none" stroke="#cadf82" stroke-width="1.6"/><rect x="1" y="3" width="15" height="4" fill="#cadf82"/><path d="M5 9h2v2H5zM9 9h2v2H9zM5 12h2v2H5zM9 12h2v2H9zM12 9h2v2h-2z" fill="#cadf82"/><path d="M5 1v3M12 1v3" stroke="#cadf82" stroke-width="1.6"/></svg>22 Dec, 2014</div>
    <h4>Lorem Ipsum is simply dummy text</h4>
    <p>Lorem Ipsum has been the industry's standard dummy text ever since the 1500s, when an unknown printer took a galley of type and scrambled it to make a type specimen book. It has survived not only five centuries,<a class="more">Read More &gt;&gt;</a></p>
  </article>

  <article class="news-item" style="left:443px">
    <div class="news-date"><svg width="17" height="17" viewBox="0 0 17 17"><rect x="1" y="3" width="15" height="13" fill="none" stroke="#cadf82" stroke-width="1.6"/><rect x="1" y="3" width="15" height="4" fill="#cadf82"/><path d="M5 9h2v2H5zM9 9h2v2H9zM5 12h2v2H5zM9 12h2v2H9zM12 9h2v2h-2z" fill="#cadf82"/><path d="M5 1v3M12 1v3" stroke="#cadf82" stroke-width="1.6"/></svg>22 Dec, 2014</div>
    <h4>Lorem Ipsum is simply dummy text</h4>
    <p>Lorem Ipsum has been the industry's standard dummy text ever since the 1500s, when an unknown printer took a galley of type and scrambled it to make a type specimen book. It has survived not only five centuries,<a class="more">Read More &gt;&gt;</a></p>
  </article>

  <article class="news-item" style="left:799px;top:152px">
    <div class="news-date"><svg width="17" height="17" viewBox="0 0 17 17"><rect x="1" y="3" width="15" height="13" fill="none" stroke="#cadf82" stroke-width="1.6"/><rect x="1" y="3" width="15" height="4" fill="#cadf82"/><path d="M5 9h2v2H5zM9 9h2v2H9zM5 12h2v2H5zM9 12h2v2H9zM12 9h2v2h-2z" fill="#cadf82"/><path d="M5 1v3M12 1v3" stroke="#cadf82" stroke-width="1.6"/></svg>22 Dec, 2014</div>
    <h4>Lorem Ipsum is simply dummy text</h4>
    <p>Lorem Ipsum has been the industry's standard dummy text ever since the 1500s, when an unknown printer took a galley of type and scrambled it to make a type specimen book. It has survived not only five centuries,<a class="more">Read More &gt;&gt;</a></p>
  </article>
</section>

<footer class="site-footer">
  <div class="footer-col" style="left:97px">
    <h5>Guest support</h5>
    <ul><li>Track your order</li><li>Shipping</li><li>Returns</li><li>Size chart</li><li>Product care</li></ul>
  </div>
  <div class="footer-col" style="left:334px">
    <h5>About us</h5>
    <ul><li>Quality stand</li><li>Faqs</li><li>Company history</li><li>Media</li><li>Investors</li></ul>
  </div>
  <div class="footer-col" style="left:553px">
    <h5>Client’s Testimonials</h5>
    <p class="testimonial">“&nbsp; Lorem Ipsum has been the industry's standard dummy text ever since the 1500s, when an unknown printer took a galley of type and scrambled it to make a type specimen book. It has survived not only five cen-</p>
    <p class="testimonial-author">Client name, City</p>
  </div>
  <div class="footer-col newsletter" style="left:872px">
    <h5>Newsletters Sign Up</h5>
    <p>Sign up for our daily email by entering your information below</p>
    <div class="email-field">Email address</div>
    <div class="subscribe-btn">SUBSCRIBE</div>
  </div>
</footer>

<div class="bottom-bar">
  <nav class="legal-links">Privacy Policy<span>|</span>Terms Conditions<span>|</span>Sitemap<span>|</span>Contact Us</nav>
  <p class="copyright">Copyright © 2014 &nbsp;All Rights Reserved</p>
  <div class="social" aria-label="Social media links">
    <span style="background:#f29b1d"></span>
    <span style="background:#2fa6de"></span>
    <span style="background:#3a5a98"></span>
    <span style="background:#4a7fd4"></span>
    <span style="background:#1d88b6"></span>
    <span style="background:#d51f26"></span>
  </div>
</div>

</body>
</html>
```